HOME PAGE AND AND SECONDARY DESIGN FOR INTERNAL PAGES

Construction company looking for an easy to navagate professional serious greyscale website with a good clean feel simple clean menu and responsive friendly design. Our main clientele is commercial properties business owners and investors of rental properties. This website is going to be static HTML5 and would need multiple sizing files for clean fast rendering. Clean and accurate design files a must so if your experienced awesome modern greyscale designer let's get started I need this done as soon as possible.

Industry/Entity Type

construction, electrical, plumbing, commercial build outs

Number of Pages Required

2 page

Font styles to use
Sans Serif

Colors

Designer to choose only greyscale colors for use in the design.

Requirements
Must have
• Main Menu... Home, Services, Projects, About our team

```html
<!DOCTYPE html>
<html lang="en">
<head>
<meta charset="utf-8">
<title>Graystone Works of Texas LLC — Home</title>
<link rel="stylesheet" href="https://fonts.googleapis.com/css2?family=Poppins:wght@400;500;600;700&display=swap">
<style>
  :root{
    --ink:#2f2f2f;
    --ink-soft:#3d3d3d;
    --paper:#e6e6e6;
    --band:#3a3a3a;
    --white:#ffffff;
    --follow:#8a8a8a;
  }
  *{box-sizing:border-box;margin:0;padding:0}
  html,body{width:1200px;height:3141px;overflow:hidden}
  body{font-family:"Poppins",sans-serif;color:var(--ink);background:var(--paper);position:relative}
  .abs{position:absolute}

  /* Hero */
  .hero{left:0;top:0;width:1200px;height:674px;background:
      radial-gradient(ellipse 260px 320px at 1080px 280px,rgba(20,20,20,.85),rgba(20,20,20,0) 100%),
      radial-gradient(ellipse 420px 260px at 420px 330px,rgba(215,215,215,.9),rgba(215,215,215,0) 100%),
      radial-gradient(ellipse 300px 200px at 880px 470px,rgba(200,200,200,.8),rgba(200,200,200,0) 100%),
      linear-gradient(180deg,#5c5c5c 0%,#6e6e6e 25%,#9d9d9d 60%,#7a7a7a 100%)}
  .brand{left:44px;top:32px;display:flex;align-items:center;gap:10px;color:var(--white)}
  .brand-dot{width:30px;height:30px;border-radius:50%;background:var(--white)}
  .brand-name{font-weight:600;font-size:17px;line-height:1;letter-spacing:.5px}
  .brand-name small{display:block;font-size:10px;letter-spacing:2.5px;font-weight:600;margin-top:4px;text-align:center}
  .nav{top:46px;right:60px;display:flex;gap:16px}
  .nav a{color:var(--white);text-decoration:none;font-size:16px;font-weight:500;line-height:22px}
  .nav a.active{border-bottom:2px solid var(--white)}
  .header-rule{left:32px;top:92px;width:1135px;height:2px;background:rgba(255,255,255,.55)}
  .hero-title{left:84px;top:286px;color:var(--white);font-weight:700;font-size:44px;line-height:53px}
  .signup{left:84px;top:411px;width:370px;height:29px;background:var(--white);display:flex;align-items:center;justify-content:space-between;padding:0 14px}
  .signup span{font-size:12px;color:#555}

  /* About */
  .about{left:0;top:674px;width:1200px;height:668px;background:var(--paper)}
  .vline{width:2px;background:#9a9a9a}
  .about h2{font-weight:700;font-size:44px;line-height:1;color:var(--ink)}
  .about-bar{left:76px;top:821px;width:148px;height:10px;background:var(--ink-soft)}
  .about p{font-size:17.5px;line-height:21px;color:var(--ink-soft)}
  .video{left:620px;top:806px;width:560px;height:375px;background:
      radial-gradient(ellipse 130px 200px at 540px 200px,#2f4a25 0%,rgba(47,74,37,0) 100%),
      radial-gradient(ellipse 170px 90px at 270px 170px,#f2f2f2 0%,rgba(242,242,242,0) 100%),
      linear-gradient(170deg,rgba(0,0,0,0) 70%,#2fb2c4 82%,#1a8fa0 100%),
      linear-gradient(180deg,#6c9fd6 0%,#a9c8e8 30%,#d9d9d4 55%,#c4c4bc 75%,#b9b9b0 100%)}
  .play{left:830px;top:930px}

  .band{left:0;width:1200px;background:var(--band)}

  /* Specialization */
  .spec-title{left:0;top:1392px;width:1200px;text-align:center;font-weight:700;font-size:56px;line-height:1;color:var(--ink)}
  .card{top:1505px;width:303px;height:419px;border-radius:22px;overflow:hidden;color:var(--white)}
  .card-arch{left:99px;background:
      linear-gradient(180deg,rgba(38,35,35,0) 55%,#262323 86%),
      radial-gradient(ellipse 150px 140px at 120px 130px,#f4f4f4,rgba(244,244,244,0) 100%),
      linear-gradient(180deg,#e0e0e0 0%,#b8b8b8 45%,#8a8a8a 70%)}
  .card-int{left:449px;background:
      linear-gradient(180deg,rgba(38,35,35,0) 55%,#262323 86%),
      radial-gradient(ellipse 140px 70px at 150px 220px,#d8d8d8,rgba(216,216,216,0) 100%),
      linear-gradient(180deg,#bcbcbc 0%,#a2a2a2 45%,#6a6a6a 70%)}
  .card-plan{left:810px;background:
      linear-gradient(180deg,rgba(38,35,35,0) 55%,#262323 86%),
      radial-gradient(ellipse 80px 120px at 230px 150px,#2a2a2a,rgba(42,42,42,0) 100%),
      linear-gradient(180deg,#7a7a7a 0%,#c8c8c8 40%,#9a9a9a 70%)}
  .card h3{position:absolute;left:15px;top:296px;font-weight:700;font-size:38px;line-height:1}
  .card p{position:absolute;left:15px;top:347px;font-size:18px;line-height:21px}

  /* Experts */
  .experts{left:0;top:2009px;width:1200px;height:802px;background:
      radial-gradient(ellipse 300px 500px at 220px 420px,rgba(30,30,30,.8),rgba(30,30,30,0) 100%),
      radial-gradient(ellipse 280px 420px at 980px 500px,rgba(40,40,40,.7),rgba(40,40,40,0) 100%),
      radial-gradient(ellipse 320px 260px at 620px 120px,rgba(150,150,150,.8),rgba(150,150,150,0) 100%),
      linear-gradient(180deg,#6a6a6a 0%,#555 45%,#3a3a3a 100%)}
  .experts h2{position:absolute;left:0;top:140px;width:1200px;text-align:center;color:var(--white);font-weight:700;font-size:54px;line-height:54px}
  .experts p{position:absolute;left:95px;top:273px;width:1010px;text-align:center;color:var(--white);font-size:14.6px;line-height:18px;font-weight:500;letter-spacing:-.1px}
  .field{position:absolute;left:368px;width:462px;height:56px;border:1.5px solid #d8d8d8;color:var(--white);font-size:19px;padding:12px 21px;font-weight:500}
  .submit{position:absolute;left:516px;top:609px;width:168px;height:29px;background:var(--white);border-radius:7px;text-align:center;color:#333;font-size:19px;letter-spacing:2.5px;line-height:29px;font-weight:500}

  /* Footer */
  .footer{left:0;top:2811px;width:1200px;height:302px;background:var(--paper)}
  .f-brand{position:absolute;left:62px;top:120px;width:180px;text-align:center;color:#7a7a7a;font-weight:600;font-size:18px;line-height:1}
  .f-brand small{display:block;font-size:11px;letter-spacing:3px;margin-top:4px}
  .f-dot{position:absolute;left:127px;top:40px;width:52px;height:52px;border-radius:50%;background:#7a7a7a}
  .f-about{position:absolute;left:62px;top:177px;width:220px;font-size:12.5px;line-height:15.5px;color:#777}
  .f-col{position:absolute;top:103px}
  .f-col h4{font-size:16px;font-weight:500;color:var(--ink);line-height:1}
  .f-col a{display:block;font-size:13px;color:#666;text-decoration:none;line-height:1}
  .f-col a:nth-of-type(1){margin-top:20px}
  .f-col a:nth-of-type(2){margin-top:17px}
  .f-col a:nth-of-type(3){margin-top:21px}
  .follow{position:absolute;left:894px;top:84px;font-weight:600;font-size:20px;color:var(--follow);line-height:1}
  .follow-bar{position:absolute;left:894px;top:110px;width:40px;height:4px;background:var(--follow)}
  .socials{position:absolute;left:896px;top:131px;display:flex;gap:20px}
  .socials span{width:32px;height:32px;border:3px solid #9a9a9a;border-radius:8px;display:block}
</style>
</head>
<body>

<section class="abs hero" role="img" aria-label="Greyscale photo of a white modern stepped house with small windows beside tall pine trees"></section>
<div class="abs brand"><span class="brand-dot"></span><div class="brand-name">GRAYSTONE WORKS<small>OF TEXAS LLC</small></div></div>
<nav class="abs nav">
  <a class="active">Home</a>
  <a>Services</a>
  <a>Projects</a>
  <a>About</a>
  <a>Gallery</a>
  <a>Properties</a>
  <a>Investment</a>
  <a>Contact</a>
</nav>
<div class="abs header-rule"></div>
<h1 class="abs hero-title">Get Ready<br>We are Finishing...</h1>
<div class="abs signup"><span>Enter Yout email id...</span>
  <svg width="18" height="10" viewBox="0 0 18 10"><path d="M0 5H16M12 1L16 5L12 9" fill="none" stroke="#444" stroke-width="1.3"/></svg>
</div>

<section class="abs about">
  <div class="abs vline" style="left:37px;top:61px;height:583px"></div>
  <div class="abs vline" style="left:593px;top:61px;height:583px"></div>
  <h2 class="abs" style="left:76px;top:80px">About the project.</h2>
  <h2 class="abs" style="left:76px;top:208px">Lorem ipsum</h2>
  <p class="abs" style="left:74px;top:287px;width:470px">Lorem ipsum dolor sit amet, consectetuer adipiscing elit, sed diam nonummy nibh euismod tincidunt ut laoreet dolore magna aliquam erat volutpat. Ut wisi enim ad minim veniam, quis nostrud exerci tation ullamcorper suscipit lobortis nisl ut aliquip ex ea commodo consequat. Duis autem vel eum iriure dolor in hendrerit in vulputate velit esse molestie consequat, vel illum dolore eu feugiat nulla facilisis at vero eros et accumsan et iusto odio dignissim qui blandit praesent luptatum zzril delenit augue duis dolore te feugait nulla facilisi.</p>
</section>
<div class="abs about-bar"></div>
<div class="abs video" role="img" aria-label="Photo of a modern white villa with glass doors beside a turquoise pool and palm trees"></div>
<svg class="abs play" width="140" height="140" viewBox="0 0 140 140" aria-hidden="true">
  <circle cx="70" cy="70" r="67" fill="none" stroke="#fff" stroke-width="3"/>
  <path d="M54 44L100 70L54 96Z" fill="#fff"/>
</svg>

<div class="abs band" style="top:1342px;height:17px"></div>

<h2 class="abs spec-title">Our Specialization</h2>
<article class="abs card card-arch" role="img" aria-label="Greyscale photo of a modern building facade seen from below">
  <h3>Architecture</h3><p>Lorem ipsum dolor sit<br>amet, consec</p>
</article>
<article class="abs card card-int" role="img" aria-label="Greyscale photo of a living room with sofa, framed prints and plants">
  <h3>Interior</h3><p>Lorem ipsum dolor sit<br>amet, consec</p>
</article>
<article class="abs card card-plan" role="img" aria-label="Greyscale photo of a hand marking a floor plan with a pen">
  <h3>Planning</h3><p>Lorem ipsum dolor sit<br>amet, consec</p>
</article>

<section class="abs experts" role="img" aria-label="Greyscale photo looking up at tall glass skyscrapers">
  <h2>DEDICATED<br>TEAM OF EXPERTS</h2>
  <p>Lorem ipsum dolor sit amet, consectetuer adipiscing elit, sed diam nonummy nibh euismod tincidunt ut laoreet dolore magna aliquam erat volutpat. Ut wisi enim ad minim veniam, quis nostrud exerci tation ullamcorper suscipit lobortis nisl ut aliquip ex ea commodo consequat. Duis autem vel eum iriure dolor in hendrerit in vulputate velit esse molestie consequat, vel illum dolore eu feugiat</p>
  <div class="field" style="top:375px">Your Name</div>
  <div class="field" style="top:451px">Your E-mail</div>
  <div class="field" style="top:528px;padding-left:40px">Contact</div>
  <div class="submit">SUBMIT</div>
</section>

<footer class="abs footer">
  <span class="f-dot"></span>
  <div class="f-brand">GRAYSTONE WORKS<small>OF TEXAS LLC</small></div>
  <p class="f-about">Lorem ipsum dolor sit amet, consectetuer adipiscing elit, sed diam nonummy nibh euismod tincidunt ut laoreet dolore magna ali</p>
  <div class="abs vline" style="left:420px;top:42px;height:238px"></div>
  <div class="abs vline" style="left:859px;top:42px;height:238px"></div>
  <div class="f-col" style="left:452px"><h4>About Us</h4><a>Our Story</a><a>Carrer</a><a>FAQ</a></div>
  <div class="f-col" style="left:592px"><h4>My Account</h4><a>Team</a><a>Sign in</a><a>Sign Out</a></div>
  <div class="f-col" style="left:734px"><h4>New Product</h4><a>Services</a><a>Specials</a><a>Offers</a></div>
  <div class="follow">follow Us</div>
  <div class="follow-bar"></div>
  <div class="socials" aria-label="Social links"><span></span><span></span><span></span><span></span><span></span></div>
</footer>

<div class="abs band" style="top:3113px;height:28px"></div>

</body>
</html>
```